Renowned Chiropractic Clinic needs unique and professional business card

We need a clean and professional looking business card that embodies our core values and stands for excellence. Highest standard of care and trustworthiness is what we want a future patient to connect to the design of the business card.
Ideally we want the design of the business card to be unique in nature and have a close connection to the SPINE as it is the core of what we do in our office - working with peoples spines.

Contact Information for Business Card

Font file is modified Nexa light and Montserrat medium. Colors are #5BC9E1, #666666, and #9dd5eb

On the front we would like to have the logo and the name of the office with an engaging, trustworthy and professional design.
On the back we need an area for our address, phone number and email address (This can be also be in the front).
On the back we would also like the slogan (this is however not a must and can also be on the front).

The HEXAGON (the design from the spine), could be an idea for the design to evolve around - this is however up to your professional creativity!

Requirements
Must have
• I want the design to primarily evolve around the HEXAGON shape and to have as few curves in it as possible. Therefore, making the design as "edgy" and "linear" as possible.

- Logo
- German Address Line (we are moving offices so we do not yet have a physical address so it would have to be a placeholder address for now that can be changed) --> Office Name (Line 1), Streetname (Line 2), Zip Code and Town (Line 3)
- email and phone number field
Nice to have
• Incorporation of the slogan "Kehren Sie Ihren Problemen den Rücken"

Please let your imagination run free :)!!! I am excited to work with you all to create an astonishing business card!

```html
<!DOCTYPE html>
<html lang="de">
<head>
<meta charset="utf-8">
<title>Linea Chiropraxis – Visitenkarte</title>
<link href="https://fonts.googleapis.com/css2?family=Montserrat:wght@400;500;600;700&display=swap" rel="stylesheet">
<style>
  :root {
    --cyan: #5BC9E1;
    --grey: #666666;
    --light-cyan: #9dd5eb;
    --white: #ffffff;
    --stage: #e9ecee;
  }
  * { box-sizing: border-box; margin: 0; padding: 0; }
  html, body {
    width: 1200px; height: 970px; overflow: hidden;
    background: var(--stage);
    font-family: "Montserrat", Arial, sans-serif;
  }
  .sheet {
    width: 1200px; height: 970px;
    display: flex; flex-direction: column; align-items: center; justify-content: center;
    gap: 40px;
  }
  .card {
    position: relative;
    width: 760px; height: 430px;
    box-shadow: 0 6px 18px rgba(0,0,0,.18);
    overflow: hidden;
  }

  /* Front */
  .card--front { background: var(--grey); }
  .front-logo {
    position: absolute; left: 0; right: 0; top: 110px;
    display: flex; align-items: center; justify-content: center; gap: 22px;
  }
  .logo-circle {
    width: 120px; height: 120px; border-radius: 50%;
    border: 2px solid var(--cyan);
  }
  .logo-name {
    color: var(--cyan); font-weight: 500; font-size: 46px; letter-spacing: 6px;
    line-height: 1;
  }
  .slogan-band {
    position: absolute; left: 0; right: 0; top: 318px; height: 32px;
    background: var(--cyan);
    display: flex; align-items: center; padding-left: 170px;
  }
  .slogan {
    color: var(--white); font-size: 17px; font-weight: 500; letter-spacing: .3px;
  }

  /* Back */
  .card--back { background: var(--white); }
  .back-logo {
    position: absolute; right: 42px; top: 48px;
    display: flex; align-items: center; gap: 16px;
  }
  .back-logo .logo-circle { width: 96px; height: 96px; }
  .back-logo .logo-name { font-size: 34px; letter-spacing: 4px; }
  .address {
    position: absolute; right: 42px; top: 196px;
    text-align: right; color: var(--grey);
    font-size: 17px; line-height: 1.35; font-weight: 500;
  }
  .divider {
    position: absolute; left: 60px; right: 42px; top: 300px;
    height: 1px; background: var(--cyan);
  }
  .person {
    position: absolute; left: 60px; top: 226px;
  }
  .person-name {
    color: var(--cyan); font-weight: 700; font-size: 33px; letter-spacing: .5px; line-height: 1;
  }
  .person-role {
    color: var(--grey); font-size: 19px; font-weight: 500; margin-top: 6px;
  }
  .contacts {
    position: absolute; left: 60px; top: 316px;
    list-style: none; color: var(--grey); font-size: 17px; font-weight: 500;
  }
  .contacts li {
    display: flex; align-items: center; gap: 16px; height: 30px;
  }
  .contacts svg { width: 20px; height: 20px; flex: none; }
</style>
</head>
<body>
<main class="sheet">

  <section class="card card--front" aria-label="Vorderseite">
    <div class="front-logo">
      <span class="logo-circle"></span>
      <span class="logo-name">LINEA</span>
    </div>
    <div class="slogan-band">
      <p class="slogan">Kehren Sie Ihren Problemen den Rücken</p>
    </div>
  </section>

  <section class="card card--back" aria-label="Rückseite">
    <div class="back-logo">
      <span class="logo-circle"></span>
      <span class="logo-name">LINEA</span>
    </div>

    <address class="address" style="font-style:normal">
      Renowned Chiropractic Clinic<br>
      Your Street Address Here<br>
      00000, German
    </address>

    <div class="person">
      <h1 class="person-name">JOHN SMITH</h1>
      <p class="person-role">Founder &amp; CEO</p>
    </div>

    <div class="divider"></div>

    <ul class="contacts">
      <li>
        <svg viewBox="0 0 24 24" aria-hidden="true"><path d="M6.6 10.8a15 15 0 0 0 6.6 6.6l2.2-2.2c.3-.3.7-.4 1-.2 1.1.4 2.3.6 3.6.6.6 0 1 .4 1 1V20c0 .6-.4 1-1 1A17 17 0 0 1 3 4c0-.6.4-1 1-1h3.5c.6 0 1 .4 1 1 0 1.3.2 2.5.6 3.6.1.3 0 .7-.2 1z" fill="var(--cyan)"/></svg>
        <span>1234567890</span>
      </li>
      <li>
        <svg viewBox="0 0 24 24" aria-hidden="true"><rect x="2" y="5" width="20" height="14" fill="none" stroke="var(--cyan)" stroke-width="2"/><path d="M2 5l10 8 10-8" fill="none" stroke="var(--cyan)" stroke-width="2"/></svg>
        <span>info@yourmail.com</span>
      </li>
      <li>
        <svg viewBox="0 0 24 24" aria-hidden="true"><circle cx="12" cy="12" r="9" fill="none" stroke="var(--cyan)" stroke-width="1.8"/><ellipse cx="12" cy="12" rx="4" ry="9" fill="none" stroke="var(--cyan)" stroke-width="1.5"/><path d="M3 12h18" stroke="var(--cyan)" stroke-width="1.5"/></svg>
        <span>www.yourwebsite.com</span>
      </li>
    </ul>
  </section>

</main>
</body>
</html>
```